Child care/Preparatory Business Card Design & logo design

I need a logo to use on a business card, letterhead, uniform and promotional material for a new business called 'Corella Kinderschool'. It is located in the north west of Western Australia in the Pilbara region. The service will provide a 'Steps Toward Schooling' program for 3 and 4 year old children. I would like a logo that shows unity, or belonging in children. I like the colour blue, any primary colours would be suitable. The design needs to be cheerful and appealing to children whilst still having an 'elite' edge to it.

Target Market(s)

Families with young children

Industry/Entity Type

Business

Contact Information for Business Card

Maren Tolling Director
Corella Kinderschool
M 0400 318 926
office@corellakinder.com.au
PO Box 591 Tarrowell WA 6735

Steps Toward Schooling

```html
<!DOCTYPE html>
<html lang="en">
<head>
<meta charset="utf-8">
<title>Corella Kinderschool — Business Card</title>
<link rel="stylesheet" href="https://fonts.googleapis.com/css2?family=Open+Sans:wght@400;600;700&display=swap">
<style>
  :root {
    --backdrop: #2b2b2d;
    --card: #f1f2f6;
    --brand-blue: #1d569b;
    --brand-pink: #d4177a;
    --accent-green: #8cbf3f;
    --text-blue: #1d4f8f;
    --white: #ffffff;
  }
  * { box-sizing: border-box; margin: 0; padding: 0; }
  html, body {
    width: 1200px; height: 816px; overflow: hidden;
    background: var(--backdrop);
    font-family: "Open Sans", Arial, sans-serif;
  }
  .business-card {
    position: absolute; left: 100px; top: 118px;
    width: 1000px; height: 580px;
    background: var(--card);
    overflow: hidden;
  }
  .card-waves { position: absolute; inset: 0; width: 100%; height: 100%; }
  .brand-mark {
    position: absolute; left: 70px; top: 150px; width: 360px;
    display: flex; align-items: center; gap: 14px;
  }
  .brand-dot {
    flex: none; width: 26px; height: 26px; border-radius: 50%;
    background: var(--accent-green);
  }
  .brand-name {
    color: var(--brand-blue); font-weight: 700;
    font-size: 40px; line-height: 1.1;
  }
  .contact-block {
    position: absolute; left: 425px; top: 112px;
    color: var(--text-blue);
  }
  .contact-name { font-size: 25px; font-weight: 700; line-height: 1.2; }
  .contact-role { font-size: 17px; color: var(--brand-pink); margin-bottom: 26px; }
  .contact-line {
    display: flex; align-items: center; gap: 8px;
    font-size: 18px; line-height: 1.5;
  }
  .contact-line svg { width: 18px; height: 18px; flex: none; }
  .contact-address { font-size: 18px; line-height: 1.7; margin-top: 22px; }
  .tagline {
    position: absolute; left: 0; right: 0; top: 492px;
    text-align: center; color: var(--white);
    font-size: 22px; font-weight: 600; letter-spacing: 4px;
    text-transform: uppercase;
  }
</style>
</head>
<body>
  <article class="business-card">
    <svg class="card-waves" viewBox="0 0 1000 580" preserveAspectRatio="none" aria-hidden="true">
      <path fill="var(--brand-pink)" d="M0 405 C 240 352 430 462 680 372 S 930 250 1000 232 L1000 580 L0 580 Z"/>
      <path fill="var(--brand-blue)" d="M0 432 C 240 382 430 490 680 402 S 930 282 1000 266 L1000 580 L0 580 Z"/>
    </svg>

    <div class="brand-mark">
      <span class="brand-dot"></span>
      <span class="brand-name">Corella<br>Kinderschool</span>
    </div>

    <div class="contact-block">
      <p class="contact-name">Maren Tolling</p>
      <p class="contact-role">Director Corella Kinderschool</p>
      <p class="contact-line">
        <svg viewBox="0 0 18 18" aria-hidden="true">
          <rect width="18" height="18" rx="3" fill="var(--brand-pink)"/>
          <path d="M5.5 4 L7.5 4 L8.2 6.6 L7 7.6 C7.6 9 8.8 10.3 10.3 11 L11.3 9.8 L13.9 10.5 L13.9 12.6 C13.9 13.2 13.4 13.6 12.8 13.5 C8.6 13 5 9.4 4.5 5.2 C4.4 4.6 4.9 4 5.5 4 Z" fill="var(--white)"/>
        </svg>
        0400 318 926
      </p>
      <p class="contact-line">
        <svg viewBox="0 0 18 18" aria-hidden="true">
          <rect x="1" y="3.5" width="16" height="11" fill="none" stroke="var(--brand-pink)" stroke-width="1.4"/>
          <path d="M1 3.5 L9 10 L17 3.5" fill="none" stroke="var(--brand-pink)" stroke-width="1.4"/>
        </svg>
        office@corellakinder.com.au
      </p>
      <p class="contact-address">PO Box 591 Tarrowell<br>WA 6735</p>
    </div>

    <p class="tagline">Steps Toward Schooling</p>
  </article>
</body>
</html>
```